Modernise Business Card

Our company has been operating for 10 years. With the start of the new decade we are looking to refresh our business card design. We manufacture a range of industrial product shipping to customers internationally. A copy of our current card, both sides, is attached. We are looking for a mature professional appearance.

```html
<!DOCTYPE html>
<html lang="en">
<head>
<meta charset="utf-8">
<title>Korvane Business Card</title>
<link rel="stylesheet" href="https://fonts.googleapis.com/css2?family=Montserrat:wght@400;600;800&display=swap">
<style>
  :root {
    --brand-blue: #03ade3;
    --logo-blue: #1f9fe0;
    --ink: #222222;
    --paper: #ffffff;
    --page: #ffffff;
    --shadow: rgba(0, 0, 0, 0.28);
  }
  * { box-sizing: border-box; margin: 0; padding: 0; }
  html, body {
    width: 1200px;
    height: 1200px;
    overflow: hidden;
    background: var(--page);
    font-family: "Montserrat", Arial, sans-serif;
    color: var(--ink);
  }
  .canvas { position: relative; width: 1200px; height: 1200px; }
  .card {
    position: absolute;
    background: var(--paper);
    box-shadow: 0 2px 9px var(--shadow);
  }
  .card--front { left: 181px; top: 78px; width: 841px; height: 480px; }
  .card--back { left: 181px; top: 622px; width: 838px; height: 478px; }

  .wordmark {
    position: absolute;
    left: 0; right: 0;
    text-align: center;
    font-weight: 800;
    font-size: 104px;
    line-height: 1;
    letter-spacing: -2px;
    color: var(--logo-blue);
  }
  .card--front .wordmark { top: 206px; }
  .card--back .wordmark { top: 96px; }

  .front-band {
    position: absolute;
    left: 0; right: 0; bottom: 0;
    height: 29px;
    background: var(--brand-blue);
  }

  .name-rule {
    position: absolute;
    top: 280px;
    height: 2px;
    background: var(--ink);
  }
  .name-rule--left { left: 30px; width: 274px; }
  .name-rule--right { left: 533px; width: 274px; }
  .person-name {
    position: absolute;
    left: 0; right: 0;
    top: 262px;
    text-align: center;
    font-weight: 600;
    font-size: 31px;
    line-height: 38px;
    color: var(--brand-blue);
  }

  .contact {
    position: absolute;
    display: flex;
    align-items: center;
    gap: 9px;
    font-size: 21.5px;
    line-height: 28px;
    color: var(--ink);
    white-space: nowrap;
  }
  .contact svg { width: 20px; height: 20px; flex: none; }
  .contact--phone-cn { left: 30px; top: 312px; }
  .contact--phone-au { left: 30px; top: 341px; }
  .contact--email { left: 450px; top: 312px; }
  .contact--web { left: 450px; top: 341px; }

  .address-band {
    position: absolute;
    left: 0; right: 0;
    top: 378px;
    height: 82px;
    background: var(--brand-blue);
    color: var(--paper);
    text-align: center;
    font-size: 20px;
    line-height: 29px;
    padding-top: 12px;
  }
</style>
</head>
<body>
<div class="canvas">
  <section class="card card--front">
    <div class="wordmark">Korvane</div>
    <div class="front-band"></div>
  </section>

  <section class="card card--back">
    <div class="wordmark">Korvane</div>

    <div class="name-rule name-rule--left"></div>
    <h1 class="person-name">Elias Brandt</h1>
    <div class="name-rule name-rule--right"></div>

    <div class="contact contact--phone-cn">
      <svg viewBox="0 0 20 20" aria-hidden="true"><path d="M4 2l3 0 1.5 4-2 1.5c1 2.2 2.8 4 5 5l1.5-2 4 1.5v3c0 1-1 2-2 2C8.5 17 3 11.5 2 4c0-1 1-2 2-2z" fill="none" stroke="#03ade3" stroke-width="1.8" stroke-linejoin="round"/><path d="M12 2.5a5.5 5.5 0 0 1 5.5 5.5M12 5.5a2.5 2.5 0 0 1 2.5 2.5" fill="none" stroke="#03ade3" stroke-width="1.5"/></svg>
      <span>+86 135 2207 4419 (China)</span>
    </div>
    <div class="contact contact--phone-au">
      <svg viewBox="0 0 20 20" aria-hidden="true"><path d="M4 2l3 0 1.5 4-2 1.5c1 2.2 2.8 4 5 5l1.5-2 4 1.5v3c0 1-1 2-2 2C8.5 17 3 11.5 2 4c0-1 1-2 2-2z" fill="none" stroke="#03ade3" stroke-width="1.8" stroke-linejoin="round"/><path d="M12 2.5a5.5 5.5 0 0 1 5.5 5.5M12 5.5a2.5 2.5 0 0 1 2.5 2.5" fill="none" stroke="#03ade3" stroke-width="1.5"/></svg>
      <span>+61 412 836 275 (Australia)</span>
    </div>
    <div class="contact contact--email">
      <svg viewBox="0 0 20 20" aria-hidden="true"><rect x="1" y="4" width="18" height="13" fill="#03ade3"/><path d="M1.5 4.5L10 11l8.5-6.5M1.5 16.5l6-5.5M18.5 16.5l-6-5.5" fill="none" stroke="#ffffff" stroke-width="1.3"/></svg>
      <span>ebrandt@korvanefittings.com</span>
    </div>
    <div class="contact contact--web">
      <svg viewBox="0 0 20 20" aria-hidden="true"><circle cx="10" cy="10" r="9" fill="#03ade3"/><path d="M5 5c2 0 3 1 2.5 3S4 9 5 12s3 1 3 4M12 3c0 2 2 2 3 3s-1 3 1 5" fill="none" stroke="#ffffff" stroke-width="1.4"/></svg>
      <span>www.korvanefittings.com</span>
    </div>

    <address class="address-band" style="font-style: normal;">
      2208-5, Lan Hua Tower, 174 Qingshi Road, Haishu District<br>
      Ningbo 315010 China
    </address>
  </section>
</div>
</body>
</html>
```